Poly Bag Packaging Motorcycle Cables - Veronzo Brand

Poly Bag Dimensions: 33cm(H) x 24cm(W)
We would like to design a genuine Poly Bag Packaging for motorcycle cables.
Veronzo, is one of the leading companies for manufacturing Motorcycles, located in Egypt. Our company is offering high-quality products, the best in the local market, with very competitive prices.
We have a limited time to get this project done, So we Highly appreciate receiving your designs ASAP.
Target Market(s)
Motorcycle Spare parts Buyers
Font styles to use
Colors
Designer to choose colors to be used in the design.
Look and feel
Each slider illustrates characteristics of the customer's brand and the style your logo design should communicate.

```html
<!DOCTYPE html>
<html lang="en">
<head>
<meta charset="utf-8">
<title>Veronzo Brake Cable Poly Bag</title>
<link rel="stylesheet" href="https://fonts.googleapis.com/css2?family=Libre+Baskerville:ital,wght@0,400;1,700&display=swap">
<style>
  :root {
    --stage: #e9e6e1;
    --bag: #f7f5f1;
    --bag-edge: #d9d5ce;
    --blue: #3d5aa8;
    --red: #d8313a;
    --yellow: #f1e23a;
    --ink: #222222;
    --white: #ffffff;
    --logo-grey: #8a8a8a;
  }
  html, body {
    margin: 0;
    padding: 0;
    width: 1200px;
    height: 1200px;
    overflow: hidden;
    background: var(--stage);
  }
  .poly-bag {
    position: absolute;
    left: 237px;
    top: 82px;
    width: 726px;
    height: 1036px;
  }
  .bag-body { fill: var(--bag); stroke: var(--bag-edge); stroke-width: 1; }
  .band-blue { fill: var(--blue); }
  .band-red { fill: var(--red); }
  .band-yellow { fill: var(--yellow); }
  .headline {
    font-family: "Libre Baskerville", serif;
    font-style: italic;
    font-weight: 700;
    font-size: 28px;
    fill: var(--white);
  }
  .label-box { fill: var(--white); }
  .product-title {
    font-family: "Libre Baskerville", serif;
    font-size: 25px;
    fill: var(--ink);
  }
  .product-meta {
    font-family: "Libre Baskerville", serif;
    font-size: 17px;
    fill: var(--ink);
  }
  .brand-dot { fill: var(--logo-grey); }
  .brand-name {
    font-family: "Libre Baskerville", serif;
    font-size: 20px;
    fill: var(--logo-grey);
    letter-spacing: 1px;
  }
  .seal-dashes {
    stroke: var(--blue);
    stroke-width: 20;
    stroke-dasharray: 58 22;
    stroke-dashoffset: 52;
  }
</style>
</head>
<body>
<svg class="poly-bag" viewBox="0 0 726 1036" xmlns="http://www.w3.org/2000/svg">
  <rect class="bag-body" x="0" y="0" width="726" height="1036"/>

  <!-- header stripes -->
  <polygon class="band-blue" points="2,58 452,58 406,178 2,178"/>
  <polygon class="band-red" points="464,58 622,58 578,178 418,178"/>
  <polygon class="band-yellow" points="622,58 726,58 726,178 590,178"/>
  <text class="headline" x="22" y="114">HIGH PERFORMANCE</text>
  <text class="headline" x="16" y="152">RACING CABLE</text>

  <!-- brand mark -->
  <circle class="brand-dot" cx="365" cy="670" r="32"/>
  <text class="brand-name" x="365" y="740" text-anchor="middle">Veronzo</text>

  <!-- label frame -->
  <polygon class="band-red" points="2,818 182,818 182,748 546,748 546,818 726,818 726,838 537,838 537,758 192,758 192,838 2,838"/>
  <polygon class="band-yellow" points="2,858 192,858 192,916 537,916 537,858 726,858 726,878 546,878 546,926 182,926 182,878 2,878"/>
  <rect class="label-box" x="202" y="758" width="324" height="150"/>
  <text class="product-title" x="364" y="800" text-anchor="middle">BRAKE CABLE</text>
  <text class="product-meta" x="364" y="841" text-anchor="middle">Model  : 0112233</text>
  <text class="product-meta" x="364" y="876" text-anchor="middle">XYZ 0123456789</text>

  <!-- seal dashes -->
  <line class="seal-dashes" x1="2" y1="966" x2="726" y2="966"/>
</svg>
</body>
</html>
```